Business card for Industrial Automation Company.

The company is called Process and Signal Dynamics. We are a systems integration company in South Africa specializing in PLC and SCADA programming, systems integration and industrial automation. Attached find logo and cover letter of the company for a feel of the general look. The website is still under development, so you will have to use your own ideas.

Please blend the colors on the business card as per the logo colors. Must be clean, professional look. Please submit a creative professional design. If a background color is used please do not use dark colored backgrounds.

Target Market(s)

Mining

Industry/Entity Type

Engineering Consultant

Contact Information for Business Card

Gerrit van Dyk (NDip Electrical LC; BSc)
Director / Systems Engineer

Postal Address
PO Box 2867
Soutkloof
7412

Physical Address:
Kloofhoek Street 27
Soutkloof
7412

Tel: +22 548 6170
Cell: +27 82 953 4086
Mail: gerritv@psd-zx.com
Web: www.psd-zx.com

Font styles to use
Sans Serif

Colors

Designer to choose colors to be used in the design.

Requirements
Must have
• Backside of the card must also contain the following:
• Services
• *Industrial Automation
• *Control System design and configuration
• *Systems Integration
• *Equipment Supply
• Industries
• *Mining
• *Factory
• *Oil and Gas
Nice to have
• Colors must blend in with colors of logo. Not too much color and no dark backgrounds.
Should not have
• dark / black background. Preferably white / light background if any.

```html
<!DOCTYPE html>
<html lang="en">
<head>
<meta charset="utf-8">
<title>Process and Signal Dynamics – Business Card</title>
<link rel="stylesheet" href="https://fonts.googleapis.com/css2?family=Source+Sans+3:wght@400;600;700&display=swap">
<style>
  :root {
    --brand-blue: #1d4a8a;
    --brand-grey: #8f9194;
    --text-grey: #7d7f82;
    --accent-lime: #c6d22b;
    --card-white: #ffffff;
    --stage: #eef0f3;
  }
  * { box-sizing: border-box; margin: 0; padding: 0; }
  html, body {
    width: 1200px; height: 900px; overflow: hidden;
    background: var(--stage);
    font-family: "Source Sans 3", Arial, sans-serif;
  }
  .canvas { position: relative; width: 1200px; height: 900px; }
  .card {
    position: absolute; width: 620px; height: 355px;
    background: var(--card-white); border-radius: 20px; overflow: hidden;
    box-shadow: 0 6px 22px rgba(0,0,0,0.12);
  }
  .card--services { left: 60px; top: 80px; }
  .card--contact { left: 520px; top: 470px; }
  .card__shapes { position: absolute; inset: 0; width: 100%; height: 100%; }

  .brand { position: absolute; left: 28px; top: 22px; display: flex; align-items: center; }
  .brand__dot { width: 34px; height: 34px; border-radius: 50%; background: var(--brand-blue); margin-right: 14px; }
  .brand__name { font-weight: 700; font-size: 80px; line-height: 1; color: var(--brand-blue); letter-spacing: -1px; }
  .brand__divider { width: 2px; height: 72px; background: var(--accent-lime); margin: 0 12px 0 14px; }
  .brand__full { font-weight: 700; font-size: 21px; line-height: 1.02; color: var(--text-grey); }
  .tagline {
    position: absolute; left: 90px; top: 106px;
    font-size: 17px; letter-spacing: 2px; color: var(--text-grey);
  }

  .industries {
    position: absolute; left: 48px; top: 150px;
    font-weight: 700; font-size: 25px; line-height: 1.1; color: var(--text-grey);
  }
  .service { position: absolute; font-weight: 600; font-size: 14px; color: #fff; white-space: nowrap; }
  .service--integration { right: 26px; top: 178px; }
  .service--supply { right: 26px; top: 200px; }
  .service--design { right: 26px; top: 318px; }
  .service--automation { left: 30px; top: 318px; }

  .person { position: absolute; left: 170px; top: 140px; text-align: center; color: var(--text-grey); font-weight: 700; }
  .person__name { font-size: 20px; line-height: 1.15; }
  .person__title { font-size: 20px; line-height: 1.15; }
  .web { position: absolute; left: 300px; top: 196px; font-weight: 700; font-size: 18px; color: var(--text-grey); }
  .contact-lines {
    position: absolute; right: 20px; top: 200px; text-align: right;
    color: #fff; font-weight: 600; font-size: 13px; line-height: 1.3;
  }
  .address {
    position: absolute; left: 26px; top: 246px;
    color: #fff; font-weight: 600; font-size: 11.5px; line-height: 1.1;
  }
  .address__group + .address__group { margin-top: 4px; }
</style>
</head>
<body>
<main class="canvas">

  <section class="card card--services" aria-label="Business card, services side">
    <svg class="card__shapes" viewBox="0 0 620 355" aria-hidden="true">
      <path fill="var(--brand-blue)" d="M0,240 C120,270 240,300 330,258 C420,216 440,118 540,108 L620,102 L620,355 L0,355 Z"/>
      <path fill="var(--brand-grey)" d="M300,355 C380,320 430,182 530,152 C570,140 600,138 620,138 L620,355 Z"/>
    </svg>
    <div class="brand">
      <span class="brand__dot"></span>
      <span class="brand__name">PSD</span>
      <span class="brand__divider"></span>
      <span class="brand__full">Process<br>and Signal<br>Dynamics</span>
    </div>
    <p class="tagline">Engineering reliable control solutions!</p>
    <p class="industries">Services for Mining,<br>Factory, Oil and Gas</p>
    <p class="service service--integration">*Systems Integration</p>
    <p class="service service--supply">*Equipment Supply</p>
    <p class="service service--design">*Control System Design and Configuration</p>
    <p class="service service--automation">*Industrial Automation</p>
  </section>

  <section class="card card--contact" aria-label="Business card, contact side">
    <svg class="card__shapes" viewBox="0 0 620 355" aria-hidden="true">
      <path fill="var(--brand-blue)" d="M0,205 C120,175 230,205 320,240 C440,270 520,150 620,90 L620,250 C540,320 450,345 360,355 L0,355 Z"/>
      <path fill="var(--brand-grey)" d="M0,232 C110,205 220,235 300,270 C350,292 380,325 400,355 L0,355 Z"/>
    </svg>
    <div class="brand">
      <span class="brand__dot"></span>
      <span class="brand__name">PSD</span>
      <span class="brand__divider"></span>
      <span class="brand__full">Process<br>and Signal<br>Dynamics</span>
    </div>
    <p class="tagline">Engineering reliable control solutions!</p>
    <div class="person">
      <p class="person__name">Gerrit van Dyk (NDip Electrical LC; BSc)</p>
      <p class="person__title">Director / Systems Engineer</p>
    </div>
    <p class="web">www.psd-zx.com</p>
    <div class="contact-lines">
      <p>+22 548 6170</p>
      <p>Cell +27 82 953 4086</p>
      <p>gerritv@psd-zx.com</p>
    </div>
    <div class="address">
      <div class="address__group">
        <p>Postal Address</p>
        <p>PO Box 2867</p>
        <p>Soutkloof 7412</p>
      </div>
      <div class="address__group">
        <p>Physical Address:</p>
        <p>Kloofhoek Street 27</p>
        <p>Soutkloof</p>
        <p>7412</p>
      </div>
    </div>
  </section>

</main>
</body>
</html>
```